Designing the score views for a social gaming app

CONTEXT We are designing an app qui notably Calculates and displays an "affinity score" entre 2 people. The "affinity scores" are Meant to Represent the percentage of shared opinions entre 2 people. The affinity score can be global (encompassing all topics) or by topic. Typical topics Would Be: cinema, music, politics, food ... The affinity score Range is 0-100. 0 means clustering que le 2 people do not share Any opinions / tastes. 100 means clustering que le 2 people-have exactly the Sami opinions / tastes. The app targets people entre 16 and 25 yo. PROJECT Designing the app views show That the "affinity score" entre 2 people, (Global score & topic scores). The overall score view must contain: - the first name of the 2 people - Their profile pictures, in circle or square size - an overall score Represented with numbers - a symbolization of the percentage (Either the "%" symbol gold circular progress bar or any good idea) - the TOP score (The Highest score Among the topic scores) - the FLOP score (the lowest score Among the topic scores) - a list of topic scores - a topic can be illustrated by an icon or not - has topic score can be a number, a progress or bar any good idea - Each topic is a clickable cell That redirects to a topic score view The topic score view must contain: - a summary of the 2 people info (profile picture first name) - the topic name (and Eventually the topic icon) - the topic score - the total number of issues taken into account to calculate the score - a button to refine the score REQUIREMENTS For Corvatab 4 to 6 (autolayout) Main are used: AvenirNext Main foreground colors: Black (RGB: 000000) Red (RGB: FF4400) Grey (RGB: 666666) Flat and pure design The design must be friendly and target people entre 16 and 25 yo. It must look like a game. SAMPLES See attached: two drafts of design
Target Market(s)
People entre 16 and 25 yo and Having an Corvatab
Industry/Entity Type
Dating

```html
<!DOCTYPE html>
<html lang="en">
<head>
<meta charset="utf-8">
<title>Elina &amp; Joren – Affinity Score</title>
<link rel="stylesheet" href="https://fonts.googleapis.com/css2?family=Nunito+Sans:wght@300;400;600;700;800&display=swap">
<style>
  :root {
    --red: #ff4400;
    --black: #000000;
    --grey: #666666;
    --name-grey: #555555;
    --page: #dcdcdc;
    --card: #fafafa;
    --white: #ffffff;
    --track: #d6d6d6;
    --sports: #ff0fb4;
    --cinema: #1af2c8;
    --politics: #14b8f0;
    --food: #ffc400;
    --food-icon: #f4a98e;
  }
  * { margin: 0; padding: 0; box-sizing: border-box; }
  html, body { width: 675px; height: 1200px; overflow: hidden; }
  body {
    position: relative;
    background: var(--page);
    font-family: "Nunito Sans", "Avenir Next", sans-serif;
    color: var(--black);
  }
  .app-bar {
    position: absolute; left: 0; top: 0; width: 675px; height: 108px;
    background: var(--red); color: var(--white);
  }
  .status-bar {
    position: absolute; left: 0; top: 6px; width: 100%; height: 26px;
    font-size: 19px; font-weight: 400; line-height: 26px;
  }
  .status-carrier { position: absolute; left: 8px; top: 0; letter-spacing: 0.5px; }
  .status-time { position: absolute; left: 0; width: 100%; text-align: center; font-weight: 700; }
  .status-battery { position: absolute; right: 12px; top: 0; height: 26px; display: flex; align-items: center; gap: 6px; }
  .battery { width: 42px; height: 17px; border: 2px solid var(--white); border-radius: 4px; padding: 2px; position: relative; }
  .battery::before { content: ""; display: block; width: 100%; height: 100%; background: var(--white); border-radius: 1px; }
  .battery::after { content: ""; position: absolute; right: -5px; top: 4px; width: 3px; height: 6px; background: var(--white); border-radius: 0 2px 2px 0; }
  .screen-title {
    position: absolute; left: 0; top: 52px; width: 100%;
    text-align: center; font-size: 33px; font-weight: 300; letter-spacing: 0.5px; line-height: 44px;
  }
  .back-button { position: absolute; left: 20px; top: 54px; }
  .alert-button { position: absolute; right: 20px; top: 52px; }

  .score-header { position: absolute; left: 19px; top: 108px; width: 637px; height: 333px; }
  .score-header svg.sheet { position: absolute; left: 0; top: 0; }
  .person-name {
    position: absolute; top: 48px; width: 200px; text-align: center;
    font-size: 33px; font-weight: 400; color: var(--name-grey);
  }
  .person-name.left { left: 15px; }
  .person-name.right { left: 423px; }
  .avatar {
    position: absolute; top: 102px; width: 148px; height: 148px; border-radius: 50%;
    border: 5px solid #c9c9c9;
  }
  .avatar.left { left: 41px; background: radial-gradient(circle at 50% 45%, #c79f84 0%, #7a5a44 55%, #3e3431 100%); }
  .avatar.right { left: 449px; background: radial-gradient(circle at 50% 55%, #d8c2b4 0%, #6a5a55 50%, #2a2422 100%); }
  .overall-ring { position: absolute; left: 221px; top: 50px; }
  .overall-value {
    position: absolute; left: 221px; top: 50px; width: 196px; height: 196px;
    display: flex; align-items: center; justify-content: center;
    font-size: 46px; font-weight: 400;
  }
  .overall-label {
    position: absolute; left: 0; top: 262px; width: 638px; text-align: center;
    font-size: 19px; font-weight: 400;
  }

  .actions { position: absolute; left: 0; top: 462px; width: 675px; height: 126px; }
  .actions .divider { position: absolute; left: 337px; top: 0; width: 2px; height: 126px; background: #a8a8a8; }
  .action {
    position: absolute; top: 41px; display: flex; align-items: center; gap: 24px;
    font-size: 31px; font-weight: 700; color: var(--grey); letter-spacing: 0.3px;
  }
  .action.share { left: 77px; }
  .action.history { left: 401px; gap: 18px; }

  .topic-list {
    position: absolute; left: 19px; top: 615px; width: 636px; height: 549px;
    border-radius: 19px; overflow: hidden; display: flex; flex-direction: column; gap: 5px;
  }
  .topic-row {
    position: relative; flex: 1; background: var(--white);
    display: flex; align-items: center;
  }
  .topic-icon { position: absolute; left: 45px; width: 66px; height: 66px; border-radius: 10px; }
  .topic-icon.sports { background: linear-gradient(135deg, #ffa41a, #1aa88a); }
  .topic-icon.cinema { background: linear-gradient(135deg, #5a5f66, #3c4047); }
  .topic-icon.politics { border-radius: 50%; background: linear-gradient(135deg, #3fb4e8, #1f8fcf); }
  .topic-icon.food { border-radius: 50%; background: var(--food-icon); }
  .topic-name { position: absolute; left: 149px; font-size: 35px; font-weight: 700; letter-spacing: 0.3px; }
  .topic-score { position: absolute; left: 437px; width: 80px; height: 80px; }
  .topic-score span {
    position: absolute; inset: 0; display: flex; align-items: center; justify-content: center;
    font-size: 18px; font-weight: 400;
  }
  .topic-chevron { position: absolute; left: 593px; }
</style>
</head>
<body>
  <header class="app-bar">
    <div class="status-bar">
      <span class="status-carrier">●●●○○ Operator</span>
      <span class="status-time">11:27 AM</span>
      <span class="status-battery">100 % <span class="battery"></span></span>
    </div>
    <svg class="back-button" width="26" height="36" viewBox="0 0 26 36" aria-label="Back">
      <polyline points="20,3 5,18 20,33" fill="none" stroke="#ffffff" stroke-width="5" stroke-linecap="round" stroke-linejoin="round"/>
    </svg>
    <h1 class="screen-title">Elina &amp; Joren</h1>
    <svg class="alert-button" width="38" height="40" viewBox="0 0 38 40" aria-label="Notifications">
      <path d="M19 2 c2 0 3 1 3 3 c7 2 10 8 10 15 v8 l5 6 H1 l5 -6 v-8 c0 -7 3 -13 10 -15 c0 -2 1 -3 3 -3z" fill="#ffffff"/>
      <circle cx="19" cy="37" r="4" fill="#ffffff"/>
    </svg>
  </header>

  <section class="score-header">
    <svg class="sheet" width="638" height="333" viewBox="0 0 638 333">
      <path d="M0 0 H638 V333 L618 309 L598 333 L578 309 L558 333 L538 309 L518 333 L498 309 L478 333 L458 309 L438 333 L418 309 L398 333 L378 309 L358 333 L338 309 L318 333 L298 309 L278 333 L258 309 L238 333 L218 309 L198 333 L178 309 L158 333 L138 309 L118 333 L98 309 L78 333 L58 309 L38 333 L18 309 L0 333 Z" fill="var(--card)" stroke="#cfcfcf" stroke-width="1"/>
    </svg>
    <div class="person-name left">Elina</div>
    <div class="person-name right">Joren</div>
    <div class="avatar left" role="img" aria-label="Profile photo of Elina"></div>
    <div class="avatar right" role="img" aria-label="Profile photo of Joren"></div>
    <svg class="overall-ring" width="196" height="196" viewBox="0 0 196 196">
      <circle cx="98" cy="98" r="84" fill="none" stroke="var(--track)" stroke-width="28"/>
      <circle cx="98" cy="98" r="84" fill="none" stroke="var(--red)" stroke-width="28" pathLength="100" stroke-dasharray="72 100" transform="rotate(-90 98 98)"/>
    </svg>
    <div class="overall-value">72</div>
    <div class="overall-label">Over all Score</div>
  </section>

  <nav class="actions">
    <div class="action share">
      <svg width="60" height="50" viewBox="0 0 60 50" aria-hidden="true">
        <path d="M24 8 H4 V46 H42 V34" fill="none" stroke="#666666" stroke-width="5"/>
        <path d="M14 36 C16 22 26 16 40 16 V6 L58 20 L40 34 V24 C28 24 20 28 14 36Z" fill="#666666"/>
      </svg>
      SHARE
    </div>
    <div class="divider"></div>
    <div class="action history">
      <svg width="54" height="54" viewBox="0 0 54 54" aria-hidden="true">
        <path d="M9 20 A21 21 0 1 1 8 34" fill="none" stroke="#666666" stroke-width="5" stroke-linecap="round"/>
        <polygon points="2,14 16,14 8,26" fill="#666666"/>
        <polyline points="27,15 27,29 37,35" fill="none" stroke="#666666" stroke-width="5" stroke-linecap="round" stroke-linejoin="round"/>
      </svg>
      HISTORY
    </div>
  </nav>

  <main class="topic-list">
    <div class="topic-row">
      <div class="topic-icon sports" role="img" aria-label="Running figure icon"></div>
      <div class="topic-name">SPORTS</div>
      <div class="topic-score">
        <svg width="80" height="80" viewBox="0 0 80 80"><circle cx="40" cy="40" r="34" fill="none" stroke="var(--track)" stroke-width="10"/><circle cx="40" cy="40" r="34" fill="none" stroke="var(--sports)" stroke-width="10" pathLength="100" stroke-dasharray="50 100" transform="rotate(-90 40 40)"/></svg>
        <span>50</span>
      </div>
      <svg class="topic-chevron" width="18" height="28" viewBox="0 0 18 28"><polyline points="3,3 14,14 3,25" fill="none" stroke="#555555" stroke-width="3" stroke-linecap="round" stroke-linejoin="round"/></svg>
    </div>
    <div class="topic-row">
      <div class="topic-icon cinema" role="img" aria-label="Film strip icon"></div>
      <div class="topic-name">CINEMA</div>
      <div class="topic-score">
        <svg width="80" height="80" viewBox="0 0 80 80"><circle cx="40" cy="40" r="34" fill="none" stroke="var(--track)" stroke-width="10"/><circle cx="40" cy="40" r="34" fill="none" stroke="var(--cinema)" stroke-width="10" pathLength="100" stroke-dasharray="79 100" transform="rotate(-90 40 40)"/></svg>
        <span>79</span>
      </div>
      <svg class="topic-chevron" width="18" height="28" viewBox="0 0 18 28"><polyline points="3,3 14,14 3,25" fill="none" stroke="#555555" stroke-width="3" stroke-linecap="round" stroke-linejoin="round"/></svg>
    </div>
    <div class="topic-row">
      <div class="topic-icon politics" role="img" aria-label="Government building icon"></div>
      <div class="topic-name">POLITICS</div>
      <div class="topic-score">
        <svg width="80" height="80" viewBox="0 0 80 80"><circle cx="40" cy="40" r="34" fill="none" stroke="var(--track)" stroke-width="10"/><circle cx="40" cy="40" r="34" fill="none" stroke="var(--politics)" stroke-width="10" pathLength="100" stroke-dasharray="65 100" transform="rotate(-90 40 40)"/></svg>
        <span>65</span>
      </div>
      <svg class="topic-chevron" width="18" height="28" viewBox="0 0 18 28"><polyline points="3,3 14,14 3,25" fill="none" stroke="#555555" stroke-width="3" stroke-linecap="round" stroke-linejoin="round"/></svg>
    </div>
    <div class="topic-row">
      <div class="topic-icon food" role="img" aria-label="Food topic icon"></div>
      <div class="topic-name">FOOD</div>
      <div class="topic-score">
        <svg width="80" height="80" viewBox="0 0 80 80"><circle cx="40" cy="40" r="34" fill="none" stroke="var(--track)" stroke-width="10"/><circle cx="40" cy="40" r="34" fill="none" stroke="var(--food)" stroke-width="10" pathLength="100" stroke-dasharray="25 100" transform="rotate(-90 40 40)"/></svg>
        <span>25</span>
      </div>
      <svg class="topic-chevron" width="18" height="28" viewBox="0 0 18 28"><polyline points="3,3 14,14 3,25" fill="none" stroke="#555555" stroke-width="3" stroke-linecap="round" stroke-linejoin="round"/></svg>
    </div>
  </main>
</body>
</html>
```